Business Card cabinets and cabinets components making company.

the card should be formal and interesting at the same time. The main colors will be black and white.

Font styles to use
Sans Serif

Colors

Designer to choose only greyscale colors for use in the design.

Requirements
Must have
• At least must have the followings:
office phone
cell phone
address
position
name
email
web

```html
<!DOCTYPE html>
<html lang="en">
<head>
<meta charset="utf-8">
<title>Panelcraft Business Card</title>
<link href="https://fonts.googleapis.com/css2?family=Roboto:wght@400;700&display=swap" rel="stylesheet">
<style>
  :root {
    --page: #4a4a4a;
    --card: #232323;
    --card-front: #1f1f1f;
    --band: #5b5b5b;
    --stripe: #2b2b2b;
    --ink: #ffffff;
    --ink-soft: #d9d9d9;
    --emboss: #7a7a7a;
    --decor: #2e2e2e;
  }
  * { margin: 0; padding: 0; box-sizing: border-box; }
  html, body { width: 799px; height: 1200px; overflow: hidden; }
  body {
    background: var(--page);
    font-family: "Roboto", sans-serif;
    position: relative;
  }
  .card {
    position: absolute;
    left: 100px;
    width: 600px;
    height: 340px;
    border-radius: 6px;
    overflow: hidden;
    box-shadow: 0 10px 30px rgba(0,0,0,.45);
  }
  .card--front { top: 140px; background: var(--card-front); }
  .card--back { top: 720px; background: var(--card); }

  .wordmark {
    position: absolute;
    display: flex;
    align-items: center;
    gap: 14px;
    font-weight: 700;
    letter-spacing: 1px;
  }
  .wordmark__square {
    width: 30px; height: 30px;
    border: 4px solid currentColor;
  }
  .wordmark__rule {
    position: absolute;
    height: 2px;
    background: currentColor;
  }
  .card--front .wordmark {
    left: 0; right: 0; top: 125px;
    justify-content: center;
    font-size: 64px;
    color: var(--emboss);
  }
  .card--front .rule-left { left: 110px; top: 210px; width: 150px; color: var(--emboss); }
  .card--front .rule-right { left: 330px; top: 210px; width: 170px; color: var(--emboss); }

  .back-band {
    position: absolute; left: 0; top: 0; bottom: 0; width: 62px;
    background: var(--band);
  }
  .back-stripe {
    position: absolute; left: 62px; top: 0; bottom: 0; width: 8px;
    background: var(--stripe);
  }
  .back-band-edge {
    position: absolute; left: 70px; top: 0; bottom: 0; width: 6px;
    background: var(--band);
  }
  .decor-square {
    position: absolute; right: 30px; top: 120px;
    width: 170px; height: 170px;
    border: 14px solid var(--decor);
  }
  .card--back .wordmark {
    left: 120px; top: 40px;
    font-size: 56px;
    color: var(--ink);
  }
  .card--back .rule-logo { left: 120px; top: 112px; width: 400px; color: var(--ink); }

  .person { position: absolute; left: 120px; top: 138px; color: var(--ink); }
  .person__name { font-size: 24px; font-weight: 700; }
  .person__role { font-size: 14px; color: var(--ink-soft); margin-top: 2px; }

  .contact {
    position: absolute; left: 120px; top: 212px;
    list-style: none; color: var(--ink);
    font-size: 15px;
  }
  .contact__row { display: flex; gap: 22px; height: 26px; align-items: center; }
  .contact__item { display: flex; align-items: center; gap: 8px; }
  .contact__item svg { width: 14px; height: 14px; fill: var(--ink); }
</style>
</head>
<body>

<section class="card card--front" aria-label="Card front">
  <div class="wordmark"><span class="wordmark__square"></span>Panelcraft</div>
  <span class="wordmark__rule rule-left"></span>
  <span class="wordmark__rule rule-right"></span>
</section>

<section class="card card--back" aria-label="Card back">
  <div class="back-band"></div>
  <div class="back-stripe"></div>
  <div class="back-band-edge"></div>
  <div class="decor-square"></div>

  <div class="wordmark"><span class="wordmark__square"></span>Panelcraft</div>
  <span class="wordmark__rule rule-logo"></span>

  <div class="person">
    <p class="person__name">Daniel Harper</p>
    <p class="person__role">Managing Director</p>
  </div>

  <ul class="contact">
    <li class="contact__row">
      <span class="contact__item">
        <svg viewBox="0 0 16 16"><path d="M3 1h3l1.5 4-2 1.2a9 9 0 0 0 4.3 4.3L11 8.5l4 1.5v3a2 2 0 0 1-2 2A13 13 0 0 1 1 3a2 2 0 0 1 2-2z"/></svg>
        555-210-4400
      </span>
      <span class="contact__item">
        <svg viewBox="0 0 16 16"><path d="M4 0h8a1 1 0 0 1 1 1v14a1 1 0 0 1-1 1H4a1 1 0 0 1-1-1V1a1 1 0 0 1 1-1zm1 2v10h6V2zm3 11a1 1 0 1 0 0 2 1 1 0 0 0 0-2z"/></svg>
        555-318-9021
      </span>
    </li>
    <li class="contact__row">
      <span class="contact__item">
        <svg viewBox="0 0 16 16"><path d="M0 3h16v10H0zm1.5 1.2v.3L8 9l6.5-4.5v-.3zM1.5 6v5.5h13V6L8 10.5z"/></svg>
        daniel@panelcraft.com
      </span>
      <span class="contact__item">
        <svg viewBox="0 0 16 16"><path d="M8 0a8 8 0 1 0 0 16A8 8 0 0 0 8 0zm5.9 7h-2.6a12 12 0 0 0-1-5 6 6 0 0 1 3.6 5zM8 2c.7.9 1.2 2.6 1.3 5H6.7C6.8 4.6 7.3 2.9 8 2zM5.7 2a12 12 0 0 0-1 5H2.1a6 6 0 0 1 3.6-5zM2.1 9h2.6a12 12 0 0 0 1 5 6 6 0 0 1-3.6-5zM8 14c-.7-.9-1.2-2.6-1.3-5h2.6c-.1 2.4-.6 4.1-1.3 5zm2.3 0a12 12 0 0 0 1-5h2.6a6 6 0 0 1-3.6 5z"/></svg>
        www.panelcraft.com
      </span>
    </li>
    <li class="contact__row">
      <span class="contact__item">
        <svg viewBox="0 0 16 16"><path d="M8 0a5.5 5.5 0 0 0-5.5 5.5C2.5 10 8 16 8 16s5.5-6 5.5-10.5A5.5 5.5 0 0 0 8 0zm0 8a2.5 2.5 0 1 1 0-5 2.5 2.5 0 0 1 0 5z"/></svg>
        18 Maple Row, Fairview, US 40210
      </span>
    </li>
  </ul>
</section>

</body>
</html>
```